Fresh pet feed direct from manufacturer to door step. Quality and Freshness un-surpassed in Industr

Need Business Card Design; leading into many other projects, for New Franchised Business Opportunity providing home delivery of fresh dog and cat feed (no emphasis needed for cat) direct from manufacturing facility. (no middle men or distributors) Food is Farm to Factory fresh. Our trademarked tagline is "Freshness is our FIRST Promise ! "
Updates

Please take note of other contest for Chirplane Cover and Profile Pic's

Target Market(s)

Dog and Cat owners

Industry/Entity Type

Pet

Contact Information for Business Card

Name, address, local phone, national 800 number, website, email address

Other font styles liked:
• follow that from logo

Requirements
Must have
• Our feed is made in Texas with ingredients sourced from local farms. We want to lean heavy on the Made in West Texas , ranch theme but that has a 'black label', 'vantrel', 'premium', 'high-end' look and feel
Nice to have
• maybe have an offer on card? 20% off with promo code "x" etc.. ?? just a thought...

```html
<!DOCTYPE html>
<html lang="en">
<head>
<meta charset="utf-8">
<title>Hale's Reserve – Business Card</title>
<link href="https://fonts.googleapis.com/css2?family=Cinzel:wght@400;600&family=Crimson+Text:wght@400;600&display=swap" rel="stylesheet">
<style>
  :root {
    --backdrop-light: #4a4e52;
    --backdrop-dark: #141516;
    --card-white: #ffffff;
    --band-ink: #221b2c;
    --band-ink-deep: #17121f;
    --gold: #b48c3a;
    --text-dark: #1d1a22;
    --text-light: #ffffff;
  }
  * { margin: 0; padding: 0; box-sizing: border-box; }
  html, body {
    width: 1200px;
    height: 900px;
    overflow: hidden;
  }
  body {
    background: radial-gradient(ellipse at 50% 30%, var(--backdrop-light) 0%, var(--backdrop-dark) 80%);
    position: relative;
  }
  .business-card {
    position: absolute;
    left: 150px;
    top: 193px;
    width: 900px;
    height: 514px;
    background: var(--card-white);
    box-shadow: 0 18px 40px rgba(0,0,0,0.55);
    overflow: hidden;
  }
  .card-bands {
    position: absolute;
    inset: 0;
    width: 900px;
    height: 514px;
  }
  .holder {
    position: absolute;
    left: 52px;
    top: 58px;
  }
  .holder-name {
    font-family: "Cinzel", serif;
    font-weight: 400;
    font-size: 31px;
    letter-spacing: 0.5px;
    color: var(--text-dark);
    line-height: 1;
  }
  .holder-role {
    font-family: "Crimson Text", serif;
    font-size: 20px;
    color: var(--gold);
    margin-top: 4px;
    letter-spacing: 0.3px;
  }
  .brand {
    position: absolute;
    left: 520px;
    top: 116px;
    display: flex;
    align-items: center;
    gap: 14px;
  }
  .brand-dot {
    width: 20px;
    height: 20px;
    border-radius: 50%;
    background: var(--text-light);
  }
  .brand-name {
    font-family: "Cinzel", serif;
    font-weight: 600;
    font-size: 35px;
    color: var(--text-light);
    letter-spacing: 1px;
    line-height: 1;
    white-space: nowrap;
  }
  .contact-list {
    position: absolute;
    left: 44px;
    top: 178px;
    list-style: none;
    font-family: "Crimson Text", serif;
    font-size: 21px;
    color: var(--text-light);
    line-height: 1.15;
  }
  .contact-list li {
    display: flex;
    align-items: flex-start;
    gap: 10px;
  }
  .contact-list .address { margin-bottom: 30px; }
  .contact-icon {
    width: 16px;
    height: 16px;
    flex: none;
    margin-top: 5px;
    fill: var(--gold);
  }
  .tagline {
    position: absolute;
    left: 0;
    right: 0;
    top: 425px;
    text-align: center;
    font-family: "Cinzel", serif;
    font-size: 23px;
    color: var(--text-dark);
    letter-spacing: 0.3px;
  }
</style>
</head>
<body>
  <article class="business-card">
    <svg class="card-bands" viewBox="0 0 900 514" aria-hidden="true">
      <defs>
        <linearGradient id="bandShade" x1="0" y1="0" x2="1" y2="1">
          <stop offset="0" stop-color="var(--band-ink)"/>
          <stop offset="1" stop-color="var(--band-ink-deep)"/>
        </linearGradient>
      </defs>
      <path class="gold-rule" d="M0 140 H430 Q460 140 475 110 Q490 84 520 84 H900" fill="none" stroke="var(--gold)" stroke-width="4"/>
      <path class="ink-band" d="M0 150 H430 Q466 150 482 118 Q496 94 522 94 H900 V400 H0 Z" fill="url(#bandShade)"/>
    </svg>

    <header class="holder">
      <h1 class="holder-name">Rowan Hale</h1>
      <p class="holder-role">Managing Director</p>
    </header>

    <div class="brand">
      <span class="brand-dot"></span>
      <span class="brand-name">Hale's Reserve</span>
    </div>

    <ul class="contact-list">
      <li class="address">
        <svg class="contact-icon" viewBox="0 0 16 16"><path d="M8 1 L15 8 H13 V15 H9.5 V10.5 H6.5 V15 H3 V8 H1 Z"/></svg>
        <span>4820 Larkspur Ridge Road<br>Ashbury VIC 3901-08</span>
      </li>
      <li>
        <svg class="contact-icon" viewBox="0 0 16 16"><path d="M3.5 1 L6 1 L7 5 L5.3 6.3 Q6.6 9.4 9.7 10.7 L11 9 L15 10 V12.5 Q15 15 12.5 15 Q1 14 1 3.5 Q1 1 3.5 1 Z"/></svg>
        <span>+ 800 555 0142</span>
      </li>
      <li>
        <svg class="contact-icon" viewBox="0 0 16 16"><path d="M1 5 Q8 0 15 5 V7 H11 V5.5 H5 V7 H1 Z M3 8 H13 L14.5 15 H1.5 Z"/></svg>
        <span>+ 999 555 0187</span>
      </li>
      <li>
        <svg class="contact-icon" viewBox="0 0 16 16"><path d="M1 3 H15 V13 H1 Z M1.5 3.5 L8 9 L14.5 3.5" stroke="var(--band-ink)" stroke-width="1"/></svg>
        <span>info@halesreserve.com</span>
      </li>
      <li>
        <svg class="contact-icon" viewBox="0 0 16 16"><circle cx="8" cy="8" r="7"/><path d="M1 8 H15 M8 1 V15 M8 1 Q3 8 8 15 M8 1 Q13 8 8 15" stroke="var(--band-ink)" stroke-width="1" fill="none"/></svg>
        <span>www.halesreserve.com</span>
      </li>
    </ul>

    <p class="tagline">“Freshness is our FIRST Promise”</p>
  </article>
</body>
</html>
```